Maple Lane Cafe & Market Squarespace Website Files

We need a Squarespace website for a new company called "Maple Lane Cafe & Market".

The company is committed to providing the highest quality, fresh and natural food, health and wellness products.

We would like to see designs that use the colors of our logo. Please provide graphic design and layout for the site.

The final design should communicate health and wellness.

Target Market(s)

Maple Lane Cafe & Market is a new company that will offer customers organic and
locally grown produce, chemical and preservative-free groceries, cruelty-free body care and eco-household products. Additionally, our kitchen will offer healthy lunch and dinner options emphasizing organic and whole food options, recognizing the trend within the restaurant industry for the demand for healthy cuisine. The restaurant will procure local foods when possible, reducing dependence on fossil fuels used for transportation. All of our products are healthy alternatives to the products available at conventional grocery chains.

Located in the heart of the growing Birchwood Avenue section of Lewiston, NY, the
marketplace will serve a community of residents in Lewiston, residents in
Niagara Falls, and residents in Niagara Falls, Ontario, Canada.

The creation of the marketplace is in response to the growing demand in the community for a local natural food store.

Industry/Entity Type

Cafe

Font styles to use
Sans Serif

Colors
00a990
faa54b
87cfc7
f37122

Requirements
Must have
• Home page, Events, Cafe Menu, Marketplace Products, Health Info, News, Recipes, Contact Us (Email form and Social Media links), Newsletter sign up.
Nice to have
• Order Online
Should not have
• (Can't think of anything right now :-)

```html
<!DOCTYPE html>
<html lang="en">
<head>
<meta charset="utf-8">
<title>Maple Lane Cafe &amp; Market</title>
<link href="https://fonts.googleapis.com/css2?family=Montserrat:wght@400;500;600&family=Open+Sans:wght@400;600&family=Noto+Serif:wght@700&display=swap" rel="stylesheet">
<style>
:root{
  --green:#8cc63f;
  --green-dark:#2f3d1f;
  --orange:#f0552a;
  --yellow:#f5d93b;
  --stone:#8e8c84;
  --band:#e3e4e6;
  --ink:#111;
  --muted:#555;
  --blue:#2a86c8;
  --white:#fff;
}
*{box-sizing:border-box;margin:0;padding:0}
html,body{width:1200px;height:1190px;overflow:hidden}
body{position:relative;background:var(--stone);font-family:"Open Sans",sans-serif;color:var(--ink)}
.abs{position:absolute}

.site-header{left:0;top:0;width:1200px;height:151px;background:var(--white)}
.brand{left:104px;top:34px;display:flex;align-items:center;gap:14px;color:var(--green);font-family:"Montserrat",sans-serif;font-weight:500}
.brand-dot{width:40px;height:40px;border-radius:50%;background:var(--green)}
.brand-name{font-size:46px;line-height:48px;letter-spacing:-.5px}
.brand-sub{display:block;font-size:13px;letter-spacing:6px;line-height:20px;margin-top:6px}
.util-nav{right:130px;top:30px;font-size:11.5px;color:#777;font-family:"Montserrat",sans-serif}
.util-nav span{margin:0 5px}
.main-nav{left:708px;top:72px;font-family:"Montserrat",sans-serif;font-size:15.5px;font-weight:500}
.main-nav a{position:absolute;top:0;white-space:nowrap;color:var(--ink);text-decoration:none}

.hero{left:0;top:151px;width:1200px;height:425px;background:linear-gradient(100deg,#b9a58c 0%,#d8cbb8 35%,#a8b870 62%,#8fae4f 80%,#c9b98f 100%)}
.hero-card{left:151px;top:252px;width:512px;height:233px;background:rgba(255,255,255,.7)}
.hero-title{left:185px;top:286px;font-family:"Montserrat",sans-serif;font-weight:500;font-size:41px;line-height:42px;color:var(--green-dark)}
.btn{display:flex;align-items:center;justify-content:center;font-family:"Montserrat",sans-serif;font-weight:500;border-radius:6px}
.btn-learn{left:184px;top:386px;width:182px;height:47px;background:var(--green);color:var(--white);font-size:19px;font-weight:600;letter-spacing:.3px}

.panel{left:59px;top:576px;width:1073px;height:517px;background:var(--white)}
.feature-img{height:155px}
.feature-title{text-align:center;font-family:"Montserrat",sans-serif;font-weight:500;font-size:17px;color:var(--orange)}
.feature-text{text-align:center;font-size:11.5px;line-height:16px;font-weight:600;color:var(--muted)}

.app-box{left:873px;top:606px;width:235px;height:287px;background:var(--green)}
.app-title{left:873px;top:616px;width:235px;text-align:center;color:var(--white);font-family:"Montserrat",sans-serif;font-size:21px}
.phone{left:930px;top:657px;width:117px;height:163px;background:#1b1b1b;border-radius:14px 14px 0 0}
.phone-screen{left:937px;top:675px;width:103px;height:145px;background:var(--white);display:flex;align-items:center;justify-content:center;text-align:center;color:var(--green);font-family:"Montserrat",sans-serif;font-weight:500;font-size:14px;line-height:16px}
.btn-app{left:902px;top:818px;width:172px;height:50px;background:var(--yellow);color:var(--ink);font-size:17px}

.coupon-band{left:81px;top:940px;width:766px;height:102px;background:var(--band)}
.coupon-label{left:102px;top:983px;font-family:"Noto Serif",serif;font-weight:700;font-size:17px;color:var(--blue)}
.coupon-input{left:256px;top:973px;width:265px;height:44px;background:var(--white);border-radius:6px;padding:12px 13px;font-family:"Montserrat",sans-serif;font-size:15px;color:#777}
.btn-signup{left:538px;top:976px;width:125px;height:41px;background:var(--green);color:var(--white);font-size:16px}
.btn-locations{left:902px;top:943px;width:172px;height:81px;background:var(--yellow);color:var(--ink);font-size:16.5px;line-height:23px;text-align:center}

.footer-text{left:102px;top:1114px;color:var(--white);font-size:12.5px;line-height:21px}
.social{top:1125px;width:20px;height:20px;border-radius:50%;background:#d7d6d1}
</style>
</head>
<body>

<header class="site-header abs">
  <div class="brand abs">
    <span class="brand-dot"></span>
    <div><span class="brand-name">Maple Lane</span><span class="brand-sub">CAFE &amp; MARKET</span></div>
  </div>
  <nav class="util-nav abs">News<span>|</span>Recipes<span>|</span>Contact Us</nav>
  <nav class="main-nav abs">
    <a style="left:0">Home</a>
    <a style="left:61px">About</a>
    <a style="left:133px">Cafe</a>
    <a style="left:192px">Products</a>
    <a style="left:281px">Health Info</a>
  </nav>
</header>

<section class="hero abs" role="img" aria-label="Salad bowl with tomatoes, radishes and peppers on a wooden table with cutlery and a measuring tape"></section>
<div class="hero-card abs"></div>
<h1 class="hero-title abs">Organic and locally<br>grown produce</h1>
<a class="btn btn-learn abs">LEARN MORE</a>

<main class="panel abs"></main>

<div class="feature-img abs" style="left:85px;top:609px;width:233px;background:linear-gradient(135deg,#2a2a2a,#d9b98a 45%,#e8d7b0 70%,#3a3a3a)" role="img" aria-label="Shrimp fried rice with chopsticks"></div>
<h2 class="feature-title abs" style="left:85px;top:776px;width:233px">Fresh Food</h2>
<p class="feature-text abs" style="left:92px;top:818px;width:219px">Need to spread the word to customers? Try Public Relations, Press Releases, and Media Kits to help reporters get the facts...when you speak at events or interviews.</p>

<div class="feature-img abs" style="left:352px;top:609px;width:230px;background:linear-gradient(135deg,#e9e9e9,#f3f1ec 40%,#d9a152 60%,#f4f4f4)" role="img" aria-label="Chicken curry with white rice on a square plate"></div>
<h2 class="feature-title abs" style="left:352px;top:776px;width:230px">healthy lunch</h2>
<p class="feature-text abs" style="left:356px;top:818px;width:222px">Need help with social media? Want your own book on Pageturn? Let our creative marketing communication pros help you.. Go to Books &amp; Blogs.</p>

<div class="feature-img abs" style="left:602px;top:609px;width:234px;background:linear-gradient(135deg,#3a3631,#d9692a 45%,#c8551e 65%,#2b2824)" role="img" aria-label="Bowl of vegetable curry with chopsticks"></div>
<h2 class="feature-title abs" style="left:602px;top:776px;width:234px">local foods</h2>
<p class="feature-text abs" style="left:606px;top:818px;width:226px">Do you treat your employees like an audience? They are! Our employee relations, employee career skills and talent development programs have helped businesses grow.</p>

<aside class="app-box abs"></aside>
<h3 class="app-title abs">Download our App</h3>
<div class="phone abs"></div>
<div class="phone-screen abs">Maple Lane</div>
<a class="btn btn-app abs">Download now</a>

<div class="coupon-band abs"></div>
<label class="coupon-label abs">Want coupons?</label>
<div class="coupon-input abs">your email</div>
<a class="btn btn-signup abs">Sign up</a>

<a class="btn btn-locations abs">Find our<br>Locations</a>

<footer>
  <p class="footer-text abs">© 2015 Maple Lane<br>Home - Site Map – FAQ – Privacy Policy – Terms of Use – Contact Us</p>
  <span class="social abs" style="left:963px" role="img" aria-label="Social link"></span>
  <span class="social abs" style="left:1005px" role="img" aria-label="Social link"></span>
  <span class="social abs" style="left:1046px" role="img" aria-label="News feed link"></span>
  <span class="social abs" style="left:1088px" role="img" aria-label="Social link"></span>
</footer>

</body>
</html>
```